Tiling Service Contractor For Custom Van Design.

I am a independent Tiling Contractor
All types of tiles, Ceramic, Porcelain, Natural Stone,
I need my van to be designed to give maximum advertising to generate more buisness and leads. I am in 2 minds, weather to have something brief and professional or go for the full wrap, I am open to all designs, you don necessary have to use my logo, as i have seen other independent contractors
Domestic & Commercial
Walls & Floor Tiler
Complete Bathroom Installations
www.cresmoraweb.ie
Email: info@cresmoraweb.ie

Target Market(s)

Everybody, house owners, other contractors

Industry/Entity Type

construction, tiling, building

Requirements
Must have
• contact info

```html
<!DOCTYPE html>
<html lang="en">
<head>
<meta charset="utf-8">
<title>Cresmora Tiling – Van Livery</title>
<link href="https://fonts.googleapis.com/css2?family=Montserrat:ital,wght@1,600;1,700;1,800&display=swap" rel="stylesheet">
<style>
  :root {
    --bg: #000000;
    --stage: #d9d9d6;
    --van-white: #f7f7f5;
    --van-trim: #3a3a38;
    --wrap-dark: #2f2e2c;
    --wrap-light: #ffffff;
    --ink: #111111;
  }
  html, body {
    margin: 0;
    padding: 0;
    width: 1200px;
    height: 378px;
    overflow: hidden;
    background: var(--bg);
  }
  .livery {
    display: block;
    width: 1200px;
    height: 378px;
  }
  .livery text {
    font-family: "Montserrat", Arial, sans-serif;
    font-style: italic;
    font-weight: 700;
    text-transform: uppercase;
  }
  .stage { fill: var(--stage); }
  .van-body { fill: var(--van-white); }
  .van-trim { fill: var(--van-trim); }
  .wrap-dark { fill: var(--wrap-dark); }
  .wrap-light { fill: var(--wrap-light); }
  .text-light { fill: var(--wrap-light); }
  .text-dark { fill: var(--ink); }
  .brand-name { font-weight: 700; }
</style>
</head>
<body>
<svg class="livery" viewBox="0 0 1200 378" xmlns="http://www.w3.org/2000/svg" aria-label="Van livery for Cresmora Tiling: side, rear and front views">

  <!-- Side view -->
  <g class="view view-side" transform="translate(12 57)">
    <rect class="stage" width="617" height="272"/>
    <path class="van-body" role="img" aria-label="White panel van, side view"
      d="M32 30 Q36 18 60 18 L395 18 Q420 18 440 30 L520 85 Q560 110 590 160 L600 200 L600 245 L35 245 Q26 240 28 220 Z"/>
    <path class="van-trim" d="M372 26 L430 28 L490 85 L480 110 L372 112 Z"/>
    <rect class="wrap-dark" x="55" y="32" width="282" height="69" rx="6"/>
    <text class="text-light" x="196" y="52" font-size="19" text-anchor="middle" textLength="260" lengthAdjust="spacingAndGlyphs" transform="rotate(1.5 196 52)">Domestic &amp; Commercial</text>
    <text class="text-light" x="196" y="69" font-size="11.5" text-anchor="middle" textLength="258" lengthAdjust="spacingAndGlyphs" transform="rotate(2 196 69)" font-weight="600">Complete Bathroom Installations</text>
    <polygon class="wrap-light" points="65,75 142,77 142,87 72,85"/>
    <text class="text-light" x="148" y="92" font-size="15" textLength="186" lengthAdjust="spacingAndGlyphs" transform="rotate(2 148 92)">Walls &amp; Floor Tiler</text>
    <polygon class="wrap-dark" points="80,103 300,112 560,150 555,158 290,120 78,110"/>
    <text class="text-dark" x="46" y="135" font-size="28" font-weight="800" textLength="285" lengthAdjust="spacingAndGlyphs" transform="rotate(4 46 135)">www.cresmoraweb.ie</text>
    <polygon class="wrap-dark" points="32,138 120,147 170,160 250,170 400,185 470,190 498,160 585,165 600,200 600,245 35,245 30,200"/>
    <polygon class="wrap-light" points="200,162 440,180 430,194 196,178"/>
    <text class="text-light" x="200" y="174" font-size="13" textLength="236" lengthAdjust="spacingAndGlyphs" transform="rotate(4 200 174)">Email: info@cresmoraweb.ie</text>
  </g>

  <!-- Rear view -->
  <g class="view view-rear" transform="translate(654 64)">
    <rect class="stage" width="264" height="254"/>
    <path class="van-body" role="img" aria-label="White panel van, rear view"
      d="M22 20 Q24 10 40 10 L224 10 Q240 10 242 20 L248 200 L248 240 L16 240 L16 200 Z"/>
    <rect class="wrap-dark" x="34" y="20" width="196" height="23" rx="4"/>
    <text class="text-light" x="132" y="37" font-size="13" text-anchor="middle" textLength="180" lengthAdjust="spacingAndGlyphs">Domestic &amp; Commercial</text>
    <text class="text-dark" x="132" y="57" font-size="13" text-anchor="middle" textLength="146" lengthAdjust="spacingAndGlyphs">Walls &amp; Floor Tiler</text>
    <path class="wrap-dark" d="M34 61 L230 61 L230 86 Q132 100 34 86 Z"/>
    <text class="text-light" x="132" y="75" font-size="13" text-anchor="middle" textLength="154" lengthAdjust="spacingAndGlyphs">Complete Bathroom</text>
    <text class="text-light" x="132" y="89" font-size="13" text-anchor="middle" textLength="102" lengthAdjust="spacingAndGlyphs">Installations</text>
    <text class="text-dark" x="132" y="110" font-size="10" text-anchor="middle" textLength="112" lengthAdjust="spacingAndGlyphs">www.cresmoraweb.ie</text>
    <rect class="wrap-dark" x="202" y="117" width="16" height="16"/>
    <text class="text-dark brand-name" x="210" y="142" font-size="4.5" text-anchor="middle">Cresmora</text>
    <path class="wrap-dark" d="M20 148 Q132 138 244 148 L244 168 L20 168 Z"/>
    <text class="text-light" x="132" y="162" font-size="11" text-anchor="middle" textLength="176" lengthAdjust="spacingAndGlyphs">Email: info@cresmoraweb.ie</text>
    <rect class="van-trim" x="18" y="222" width="228" height="18"/>
  </g>

  <!-- Front view -->
  <g class="view view-front" transform="translate(934 68)">
    <rect class="stage" width="238" height="245"/>
    <path class="van-body" role="img" aria-label="White panel van, front view"
      d="M30 20 Q40 6 70 6 L168 6 Q198 6 208 20 L222 110 L228 160 L228 235 L10 235 L10 160 L16 110 Z"/>
    <path class="van-trim" role="img" aria-label="Windscreen" d="M40 18 L198 18 L214 72 Q119 66 24 72 Z"/>
    <rect class="wrap-dark" x="110" y="96" width="18" height="18"/>
    <text class="text-dark brand-name" x="119" y="122" font-size="5" text-anchor="middle">Cresmora</text>
    <path class="wrap-dark" d="M10 160 Q119 176 228 160 L228 235 L10 235 Z"/>
  </g>

</svg>
</body>
</html>
```